Business cards, envelopes, etc. for real estate company

We have a finished logo for our real estate company. We need a corporate identity package with the following items:

1. Business Cards
2. Letterhead/Stationary - with 2 pages:
-1st page with full header
-2nd page without top header
3. Concise and professional e-mail signature image
4. Fax coversheet
5. Shipping label, with our return address and a mail-to address (on one label)

We need these to be editable. We don't know the industry standard for these items but perhaps you can provide them to us in .PDF and Word format (and if you use Adobe Illustrator for them, .AI as well).

Please use the attached placeholder logo in your design entry. We will provide you with the original logo to swap in (same size and design, just different text) when we choose your entry.

Please include the following information on the letterhead and business cards:

58 West 41st Street
3rd Floor West
New York, NY 10047

Tel: 212-555-0148
Fax :212-555-0148

Please contact us if you have any questions about this contest.
Updates

Hi,

Thanks for your interest in this project. The logo to use should be working now. Please contact me if you have any further issues or questions.

I look forward to seeing your submissions. 

Hi,

We first wish to thank you all for your submissions. 

Here is some general feedback regarding the designs shown:

1. We would prefer square (as opposed to rounded) business cards.

2. For the fax coversheets, we are looking with a designed look. While we understand these are samples, we don't want it to appear as if it a standard block of text or a fax template from a word processing program.

3. For the 1st page of letterhead and envelopes, we do need an office address on them. The envelopes should have space for a stamp in the top right corner. We would prefer the envelopes not to have colored stripes.

4. We think a watermark of the logo is an interesting idea on the business cards and/or letterhead. This may be something to try. However, it is not strictly necessary and we would like to evaluate designs with and without it.

In general we are looking for a clean yet professional look.

We are actively reviewing all entries and thank you for your time and creativity.

One last comment: We understand making all objects in the brief takes some time. However, we want to remind all the designers that this contest is for more than just business cards (envelopes, letterheads, etc.) so if we choose your design, those items will be expected. Please refer to the original brief to see what we are requesting.

If you provide a mockup of any item listed in the brief (in addition to business cards) it would help us visualize your entire vision for this project.

Industry/Entity Type

Real Estate

```html
<!DOCTYPE html>
<html lang="en">
<head>
<meta charset="utf-8">
<title>Brookmere Realty — Stationery Set</title>
<link href="https://fonts.googleapis.com/css2?family=Lato:wght@300;400;700&display=swap" rel="stylesheet">
<style>
  :root {
    --backdrop: #d7d7d7;
    --band-1: #2e6797;
    --band-2: #255684;
    --band-3: #1f476d;
    --band-4: #1a3a5a;
    --band-5: #162f48;
    --band-6: #13273b;
    --paper: #ffffff;
    --logo-panel: #f2f2f2;
    --brand-navy: #1f476d;
    --ink-soft: #9aa0a6;
    --card-text-light: #c9d6e3;
  }
  * { box-sizing: border-box; margin: 0; padding: 0; }
  html, body { width: 1200px; height: 899px; overflow: hidden; }
  body {
    background: var(--backdrop);
    font-family: "Lato", Arial, sans-serif;
    position: relative;
  }

  .banded {
    background: linear-gradient(to bottom,
      var(--band-1) 0%, var(--band-2) 20%,
      var(--band-2) 20%, var(--band-3) 38%,
      var(--band-4) 38%, var(--band-4) 56%,
      var(--band-5) 56%, var(--band-5) 76%,
      var(--band-6) 76%, var(--band-6) 100%);
  }

  .brand {
    display: flex;
    align-items: center;
    gap: 0.45em;
    background: var(--logo-panel);
    white-space: nowrap;
  }
  .brand-square {
    width: 1.3em;
    height: 1.3em;
    background: var(--brand-navy);
    flex: none;
  }
  .brand-name {
    color: var(--brand-navy);
    font-weight: 700;
    line-height: 1;
    letter-spacing: 0.02em;
  }

  /* Letterhead cover */
  .letterhead {
    position: absolute;
    left: 610px; top: 100px;
    width: 480px; height: 690px;
    box-shadow: 0 6px 18px rgba(0,0,0,0.18);
  }
  .letterhead .brand {
    position: absolute;
    right: 0; top: 265px;
    width: 250px; height: 76px;
    padding: 0 20px;
    font-size: 20px;
  }

  /* Notepad */
  .notepad {
    position: absolute;
    left: 150px; top: 60px;
    width: 270px; height: 370px;
    box-shadow: 0 4px 0 #eeeeee, 0 8px 16px rgba(0,0,0,0.18);
  }
  .notepad .spiral {
    position: absolute;
    left: 30px; top: -10px;
    width: 210px; height: 20px;
  }
  .notepad .brand {
    position: absolute;
    left: 50px; top: 124px;
    width: 170px; height: 46px;
    padding: 0 12px;
    font-size: 13px;
  }

  /* Business cards */
  .card {
    position: absolute;
    width: 330px; height: 188px;
    box-shadow: 0 3px 0 #e6e6e6, 0 6px 0 #dcdcdc, 0 10px 16px rgba(0,0,0,0.16);
  }
  .card-white { left: 120px; top: 470px; background: var(--paper); }
  .card-blue {
    left: 120px; top: 685px;
    background: linear-gradient(160deg, var(--band-1) 0%, var(--band-3) 55%, var(--band-5) 100%);
  }
  .card .address {
    position: absolute;
    left: 194px; top: 22px;
    font-size: 8px;
    line-height: 1.35;
    width: 110px;
  }
  .card .brand {
    position: absolute;
    left: 170px; top: 96px;
    font-size: 14px;
    background: transparent;
  }
  .card .person { position: absolute; left: 26px; top: 100px; }
  .card .person-name {
    font-weight: 700;
    font-size: 10px;
    letter-spacing: 0.06em;
    text-transform: uppercase;
  }
  .card .person-title { font-size: 8px; margin-top: 2px; }

  .card-white .address { color: var(--ink-soft); }
  .card-white .person-name { color: var(--brand-navy); }
  .card-white .person-title { color: var(--ink-soft); }

  .card-blue .address,
  .card-blue .person-title { color: var(--card-text-light); }
  .card-blue .person-name { color: var(--paper); }
  .card-blue .brand-square { background: var(--paper); }
  .card-blue .brand-name { color: var(--paper); }
</style>
</head>
<body>

  <section class="notepad banded" aria-label="Notepad cover">
    <svg class="spiral" viewBox="0 0 210 20" aria-hidden="true">
      <g fill="none" stroke="#1b1b1b" stroke-width="2">
        <ellipse cx="6" cy="10" rx="4" ry="8"/><ellipse cx="24" cy="10" rx="4" ry="8"/>
        <ellipse cx="42" cy="10" rx="4" ry="8"/><ellipse cx="60" cy="10" rx="4" ry="8"/>
        <ellipse cx="78" cy="10" rx="4" ry="8"/><ellipse cx="96" cy="10" rx="4" ry="8"/>
        <ellipse cx="114" cy="10" rx="4" ry="8"/><ellipse cx="132" cy="10" rx="4" ry="8"/>
        <ellipse cx="150" cy="10" rx="4" ry="8"/><ellipse cx="168" cy="10" rx="4" ry="8"/>
        <ellipse cx="186" cy="10" rx="4" ry="8"/><ellipse cx="204" cy="10" rx="4" ry="8"/>
      </g>
    </svg>
    <div class="brand">
      <span class="brand-square"></span>
      <span class="brand-name">Brookmere Realty</span>
    </div>
  </section>

  <section class="card card-white" aria-label="Business card, front">
    <p class="address">58 West 41st Street<br>3rd Floor West<br>New York, NY 10047<br>Phone: 212-555-0148<br>Fax: 212-555-0148</p>
    <div class="brand">
      <span class="brand-square"></span>
      <span class="brand-name">Brookmere Realty</span>
    </div>
    <div class="person">
      <p class="person-name">Owen Carter</p>
      <p class="person-title">Managing Director</p>
    </div>
  </section>

  <section class="card card-blue" aria-label="Business card, reverse">
    <p class="address">58 West 41st Street<br>3rd Floor West<br>New York, NY 10047<br>Phone: 212-555-0148<br>Fax: 212-555-0148</p>
    <div class="brand">
      <span class="brand-square"></span>
      <span class="brand-name">Brookmere Realty</span>
    </div>
    <div class="person">
      <p class="person-name">Owen Carter</p>
      <p class="person-title">Managing Director</p>
    </div>
  </section>

  <section class="letterhead banded" aria-label="Letterhead cover">
    <div class="brand">
      <span class="brand-square"></span>
      <span class="brand-name">Brookmere Realty</span>
    </div>
  </section>

</body>
</html>
```